Poster Design

Hello,

My name is Rowan Pickett and I run a vidora channel called 'CrumbleDiary'. I want a poster made for those who watch my video to purchase and put on their wall at home. The poster will be all text and as you can see, I've attached a few examples of posters which I would like it to be similar to. I use a lot of the colour #ab6f7f so it would be good to incorporate this in somewhere (maybe the background colour).
I would like the poster to say:
"Do More Of What Makes YOU Happy"
I need this poster to be for sale ready for christmas, so Im going to need the designs created as soon as possible. Im sorry for the rush.
Have fun with it and feel free to upload multiple versions of a design as well as a few designs if you like.
I look forward to seeing what you come up with.
Rowan
(Of course I will need to own all rights once the payment has been made)

```html
<!DOCTYPE html>
<html lang="en">
<head>
<meta charset="utf-8">
<title>Do More Of What Makes You Happy — Poster</title>
<link rel="stylesheet" href="https://fonts.googleapis.com/css2?family=Anton&family=Damion&family=Josefin+Sans:wght@200;300&family=Marcellus&family=Yellowtail&display=swap">
<style>
  :root {
    --backdrop: #e8e5e1;
    --poster-dark: #101010;
    --poster-mid: #2a2a2a;
    --poster-glow: #8d8d8d;
    --ink: #ffffff;
    --brand: #ab6f7f;
  }
  html, body {
    margin: 0;
    padding: 0;
    width: 968px;
    height: 1200px;
    overflow: hidden;
    background: var(--backdrop);
  }
  .canvas {
    position: relative;
    width: 968px;
    height: 1200px;
  }
  .poster-art {
    position: absolute;
    inset: 0;
    width: 968px;
    height: 1200px;
    display: block;
  }
  .word-do { font-family: "Josefin Sans", sans-serif; font-weight: 200; font-size: 118px; fill: var(--ink); }
  .word-more-of { font-family: "Anton", sans-serif; font-size: 102px; fill: var(--ink); }
  .word-what { font-family: "Damion", "Yellowtail", cursive; font-size: 104px; fill: var(--ink); }
  .word-makes { font-family: "Josefin Sans", sans-serif; font-weight: 300; font-size: 54px; fill: var(--ink); }
  .word-you { font-family: "Anton", sans-serif; font-size: 32px; letter-spacing: 14px; fill: var(--brand); }
  .word-happy { font-family: "Marcellus", serif; font-size: 124px; fill: var(--ink); }
  .rule, .star, .highlight-bar { fill: var(--ink); }
</style>
</head>
<body>
<div class="canvas">
  <svg class="poster-art" viewBox="0 0 968 1200" xmlns="http://www.w3.org/2000/svg" aria-label="Do more of what makes you happy">
    <defs>
      <radialGradient id="poster-light" cx="484" cy="240" r="520" gradientUnits="userSpaceOnUse">
        <stop offset="0" stop-color="#8d8d8d"/>
        <stop offset="0.45" stop-color="#2a2a2a"/>
        <stop offset="1" stop-color="#101010"/>
      </radialGradient>
      <polygon id="star" class="star" points="0,-6 1.5,-2 6,-2 2.4,0.8 3.7,5.2 0,2.6 -3.7,5.2 -2.4,0.8 -6,-2 -1.5,-2"/>
    </defs>

    <rect class="poster-sheet" x="155" y="135" width="657" height="928" fill="url(#poster-light)"/>

    <g class="heading-do">
      <rect class="rule" x="273" y="324" width="136" height="8"/>
      <rect class="rule" x="273" y="400" width="136" height="8"/>
      <rect class="rule" x="580" y="324" width="114" height="8"/>
      <rect class="rule" x="580" y="400" width="114" height="8"/>
      <use href="#star" x="283" y="368"/>
      <use href="#star" x="310" y="368"/>
      <use href="#star" x="337" y="368"/>
      <use href="#star" x="364" y="368"/>
      <use href="#star" x="391" y="368"/>
      <use href="#star" x="597" y="368"/>
      <use href="#star" x="621" y="368"/>
      <use href="#star" x="645" y="368"/>
      <use href="#star" x="669" y="368"/>
      <use href="#star" x="692" y="368"/>
      <text class="word-do" x="410" y="410" textLength="170" lengthAdjust="spacingAndGlyphs">DO</text>
    </g>

    <text class="word-more-of" x="273" y="530" textLength="421" lengthAdjust="spacingAndGlyphs">MORE OF</text>

    <text class="word-what" x="362" y="640" textLength="192" lengthAdjust="spacingAndGlyphs">what</text>

    <rect class="rule" x="273" y="656" width="421" height="2"/>
    <text class="word-makes" x="273" y="712" textLength="423" lengthAdjust="spacing">MAKES</text>
    <rect class="rule" x="273" y="718" width="421" height="2"/>

    <rect class="highlight-bar" x="273" y="735" width="421" height="38"/>
    <text class="word-you" x="490" y="767" text-anchor="middle">YOU</text>

    <text class="word-happy" x="271" y="878" textLength="423" lengthAdjust="spacingAndGlyphs">HAPPY</text>
  </svg>
</div>
</body>
</html>
```